Velt Risk Management - Harbor Pathway

Upgrade existing PP per the upload. I will use this to email to Prospects and clients as well as posting to our website.
Edit and update pages - this PP was created several years ago and needs a full update based on the same content. Better graphics etc etc are needed
Create some links to websites
Velt Risk Management is a professional consultant where owners have MBA's. Law Degrees and CPCU Designation. PP should be designed with this in mind similar to resources used by CPA's, Accountants or Financial Advisors
Updates
Need extra days to review
Target Market(s)
Construction Contractors
Colors
Designer to choose colors to be used in the design.
Requirements
Must have
- Follow existing PP
Nice to have
- Take a look at our current website which will be upgraded when PP is complete
- www.tarvelpointe.biz

```html
<!DOCTYPE html>
<html lang="en">
<head>
<meta charset="utf-8">
<title>Velt Risk Management - Harbor Pathway</title>
<link href="https://fonts.googleapis.com/css2?family=Fira+Sans:wght@300;400;600;700&family=Fira+Sans+Condensed:wght@400;600&family=Lato:wght@300;400;700&display=swap" rel="stylesheet">
<style>
:root{
  --board:#adadad;
  --slide:#ffffff;
  --orange:#e8790f;
  --amber:#f7a11a;
  --amber-soft:rgba(250,180,70,.75);
  --teal:#4db6ac;
  --teal-dark:#2e9f8f;
  --green:#1e9a63;
  --lilac:#c98ee0;
  --ink:#444;
  --ring:#d3e6f2;
}
*{margin:0;padding:0;box-sizing:border-box}
html,body{width:1200px;height:1000px;overflow:hidden;background:var(--board)}
body{position:relative;font-family:"Lato",Arial,sans-serif;color:var(--ink)}
.slide{position:absolute;width:372px;height:209px;background:var(--slide);overflow:hidden}
.slide.has-bar::after{content:"";position:absolute;left:0;right:0;bottom:0;height:4px;background:var(--teal)}
.page-no{position:absolute;right:8px;bottom:8px;font-size:4px;color:#999}
.abs{position:absolute}
.rule{position:absolute;height:1px;background:var(--teal)}
.brand-title{position:absolute;left:0;right:0;top:70px;text-align:center;font-family:"Fira Sans",sans-serif;font-weight:700;font-size:22px;color:var(--orange);letter-spacing:.2px}
.brand-sub{position:absolute;left:0;right:0;top:100px;text-align:center;font-size:5.5px;font-weight:700;color:var(--amber)}
.brand-url{position:absolute;left:0;right:0;top:121px;text-align:center;font-size:10px;color:var(--ink)}
.h-orange{position:absolute;font-family:"Fira Sans Condensed",sans-serif;font-weight:600;color:var(--orange);font-size:17px}
.h-light{position:absolute;font-family:"Fira Sans",sans-serif;font-weight:300;color:var(--amber)}
.list{position:absolute;list-style:none;font-size:9.5px;line-height:16.5px;color:var(--ink);font-weight:400}
.list li{padding-left:18px;position:relative}
.arrows li::before{content:"→";position:absolute;left:0;font-size:9px}
.alpha{counter-reset:a}
.alpha li{counter-increment:a}
.alpha li::before{content:counter(a,upper-alpha) ".";position:absolute;left:2px}
.philosophy{position:absolute;left:22px;top:104px;width:335px;font-size:7px;line-height:13px;color:var(--teal-dark)}
.deco{position:absolute;border-radius:50%}
.portrait{position:absolute;left:14px;width:132px;height:171px}
.frame{position:absolute;border:1px solid}
.frame.t{border-color:var(--teal)}
.frame.o{border-color:var(--orange)}
.quote{position:absolute;font-size:7px;line-height:11px;text-align:center;color:var(--ink)}
.person{position:absolute;right:30px;top:128px;font-family:"Fira Sans Condensed",sans-serif;font-weight:600;font-size:16px;color:var(--orange)}
.tiny{position:absolute;font-size:5.5px;line-height:7px;color:var(--ink)}
.gbox{position:absolute;width:50px;height:26px;background:var(--teal);color:#fff;font-size:5px;display:flex;align-items:center;justify-content:center}
.nav-title{position:absolute;left:0;right:0;top:18px;text-align:center;font-size:8px;color:var(--ink)}
.nav-tag{position:absolute;color:#fff;font-size:5.5px;line-height:6px;text-align:center;padding:2px 0}
.nav-card{position:absolute;background:#fff;box-shadow:0 0 3px rgba(0,0,0,.12);font-size:5px;line-height:7px;padding:4px 0 0 8px}
</style>
</head>
<body>

<section class="slide" style="left:27px;top:19px">
  <div class="rule" style="left:41px;width:288px;top:41px"></div>
  <div class="brand-title">KEELSTONE BUILD</div>
  <div class="brand-sub">Management Consultants for the Construction Industry</div>
  <div class="rule" style="left:64px;width:24px;top:128px"></div>
  <div class="brand-url">www.tarvelpointe.biz</div>
  <div class="rule" style="left:284px;width:24px;top:128px"></div>
  <div class="rule" style="left:41px;width:288px;top:167px"></div>
</section>

<section class="slide has-bar" style="left:416px;top:19px">
  <h2 class="h-orange" style="left:16px;top:22px">Mission Statement</h2>
  <ul class="list arrows" style="left:20px;top:56px;width:335px">
    <li>To provide the highest level of personal financial services in a friendly, professional manner</li>
    <li>To encourage contractor clients to establish and extend effective management systems in their companies</li>
    <li>To increase the knowledge and ability of our clients to manage and control their financial well-being</li>
    <li>To provide sound financial/operating management advice in order to maximize clients corporate value while minimizing risk</li>
  </ul>
</section>

<section class="slide" style="left:805px;top:19px">
  <div class="deco" style="left:283px;top:-4px;width:80px;height:80px;background:var(--amber)"></div>
  <div class="deco" style="left:268px;top:20px;width:76px;height:76px;background:var(--amber-soft)"></div>
  <h2 class="h-light" style="left:23px;top:38px;font-size:18px">Keelstone Build Philosophy:</h2>
  <p class="philosophy">Keelstone Build is dedicated to the safe and successful growth of their construction clients by strategically implementing comprehensive and practical management systems. KB will minimize business risk by maximizing critical information flows to the CEO throughout the organization. KB will provide the Client CEO with the necessary tools for the critical information needed to manage his growing company. The objective is to maximize company value and minimize business risk.</p>
</section>

<section class="slide" style="left:27px;top:247px">
  <div class="nav-title" style="top:20px">Goals and Objectives</div>
  <svg class="abs" style="left:0;top:0" width="372" height="209" aria-hidden="true">
    <circle cx="186" cy="116" r="58" fill="none" stroke="var(--ring)" stroke-width="6"/>
    <path d="M158 62 l8 -6 l-1 10 z" fill="var(--ring)"/>
  </svg>
  <div class="gbox" style="left:160px;top:61px">1</div>
  <div class="gbox" style="left:208px;top:101px">2</div>
  <div class="gbox" style="left:190px;top:153px">3</div>
  <div class="gbox" style="left:136px;top:153px">4</div>
  <div class="gbox" style="left:111px;top:101px">5</div>
  <div class="tiny" style="left:226px;top:62px;width:76px">Review Why Contractors Fail</div>
  <div class="tiny" style="left:268px;top:104px;width:82px">Focus on Why Contractors Succeed</div>
  <div class="tiny" style="left:252px;top:153px;width:70px">Establish Basic Premise: Knowledge/Education/ Commitment to Change will improve the bottom line</div>
  <div class="tiny" style="left:46px;top:153px;width:84px;text-align:right">Implement Contractors Navigation System to accomplish Mission Statement</div>
  <div class="tiny" style="left:28px;top:102px;width:78px;text-align:right">Support Client in the continuing commitment to use the integrated Management model</div>
</section>

<section class="slide has-bar" style="left:416px;top:247px">
  <h2 class="h-orange" style="left:16px;top:22px">Basic Assumptions</h2>
  <ol class="list alpha" style="left:18px;top:56px;width:340px">
    <li>Construction Companies need to be Micro Managed.</li>
    <li>Construction Companies Require a High Level of Standardization in a Non Standardized Industry.</li>
    <li>Manage the Negative Variances.</li>
    <li>Construction Companies fall into Project Based or Management Based Models.</li>
    <li>Growing Construction Companies require the proper balance between Leadership and Management.</li>
  </ol>
</section>

<section class="slide" style="left:805px;top:247px">
  <div class="deco" style="left:283px;top:-4px;width:80px;height:80px;background:var(--amber)"></div>
  <div class="deco" style="left:268px;top:20px;width:76px;height:76px;background:var(--amber-soft)"></div>
  <h2 class="h-light" style="left:23px;top:90px;font-size:22px">Leadership / Management</h2>
  <span class="page-no">6</span>
</section>

<section class="slide has-bar" style="left:27px;top:475px">
  <div class="portrait" style="top:18px;background:linear-gradient(160deg,#6b4a2e,#3a2a1c 60%,#8a6a4c)" role="img" aria-label="Portrait photograph of Daniel Ashford in a library"></div>
  <div class="frame t" style="left:158px;top:48px;width:177px;height:49px"></div>
  <div class="frame o" style="left:168px;top:65px;width:178px;height:55px"></div>
  <p class="quote" style="left:166px;top:76px;width:180px">"Leaders set the course for the whole team"<br>"Managers keep the daily work on track"</p>
  <div class="person">Daniel Ashford</div>
  <span class="page-no">7</span>
</section>

<section class="slide has-bar" style="left:416px;top:475px">
  <div class="portrait" style="top:18px;background:linear-gradient(160deg,#2f6fae,#1c3c66 55%,#3d4a5a)" role="img" aria-label="Portrait photograph of Marcus Lindqvist speaking"></div>
  <div class="frame t" style="left:158px;top:48px;width:177px;height:49px"></div>
  <div class="frame o" style="left:168px;top:65px;width:178px;height:55px"></div>
  <p class="quote" style="left:166px;top:76px;width:180px">"Leadership is about earning trust"<br>"Management is about keeping promises on time"</p>
  <div class="person">Marcus Lindqvist</div>
  <span class="page-no">8</span>
</section>

<section class="slide has-bar" style="left:805px;top:475px">
  <div class="portrait" style="top:18px;background:linear-gradient(160deg,#d6d6d6,#6f6f6f 60%,#9a9a9a)" role="img" aria-label="Black and white portrait photograph of Theodore Vance"></div>
  <div class="frame t" style="left:158px;top:48px;width:190px;height:49px"></div>
  <div class="frame o" style="left:168px;top:65px;width:190px;height:55px"></div>
  <p class="quote" style="left:172px;top:74px;width:182px">"Leaders care about where the company is heading"<br>"Managers care about how each job is delivered"</p>
  <div class="person" style="right:14px">Theodore Vance</div>
  <span class="page-no">9</span>
</section>

<section class="slide has-bar" style="left:27px;top:703px">
  <div class="portrait" style="top:20px;background:linear-gradient(160deg,#e4e4e4,#4a4a4a 60%,#c9c9c9)" role="img" aria-label="Portrait photograph of Samuel Okafor in a dark suit"></div>
  <div class="frame t" style="left:158px;top:50px;width:176px;height:50px"></div>
  <div class="frame o" style="left:168px;top:68px;width:176px;height:50px"></div>
  <p class="quote" style="left:166px;top:82px;width:178px">"Leaders draw the plans"<br>"Managers pour the foundation"</p>
  <div class="person" style="top:130px">Samuel Okafor</div>
  <span class="page-no">10</span>
</section>

<section class="slide has-bar" style="left:416px;top:703px">
  <div class="portrait" style="top:16px;background:linear-gradient(160deg,#b98a55,#4a3a2a 55%,#2a2f4a)" role="img" aria-label="Portrait photograph of Richard Hale in suit and tie"></div>
  <div class="frame t" style="left:159px;top:46px;width:190px;height:57px"></div>
  <div class="frame o" style="left:163px;top:65px;width:198px;height:58px"></div>
  <p class="quote" style="left:166px;top:72px;width:186px">"Leadership focuses on setting a shared direction"<br>"Management is the planning of work, it's about follow-through"</p>
  <div class="person" style="right:16px;top:126px">Richard Hale</div>
  <span class="page-no">11</span>
</section>

<section class="slide" style="left:805px;top:703px">
  <div class="nav-title">Keelstone Harbor Pathway</div>
  <div class="rule" style="left:176px;width:20px;top:33px;background:var(--orange);height:1.5px"></div>
  <svg class="abs" style="left:0;top:0" width="372" height="209" aria-hidden="true">
    <path d="M152 75 Q190 42 220 68" fill="none" stroke="#ddd" stroke-width="2"/>
    <path d="M72 160 Q110 190 150 150" fill="none" stroke="#ddd" stroke-width="2"/>
    <path d="M230 150 Q270 190 300 120" fill="none" stroke="#ddd" stroke-width="2"/>
  </svg>
  <div class="nav-card" style="left:28px;top:90px;width:74px;height:52px">• Estimating<br>• Scheduling<br>• Field Oversight</div>
  <div class="nav-tag" style="left:36px;top:131px;width:58px;background:var(--lilac)">Project<br>Management</div>
  <div class="nav-card" style="left:115px;top:78px;width:62px;height:64px;padding-top:26px">• Planning<br>• HR</div>
  <div class="nav-tag" style="left:116px;top:78px;width:57px;background:var(--green)">General<br>Managment</div>
  <div class="nav-card" style="left:205px;top:96px;width:70px;height:46px">• Insurance<br>• Safety<br>• Legal</div>
  <div class="nav-tag" style="left:207px;top:132px;width:57px;background:var(--teal)">Risk<br>Management</div>
  <div class="nav-card" style="left:284px;top:79px;width:68px;height:50px;padding-top:26px">• Finance<br>• Accounting</div>
  <div class="nav-tag" style="left:285px;top:79px;width:58px;background:var(--amber)">Financial<br>Managment</div>
</section>

</body>
</html>
```